Business Card for my New Brokerage

Looking to get a business card design for my new Real Estate Brokerage.
I want it with Picture, Phone Number, Email, Website, Office Address
Name and Designation. Please add logo too.

Target Market(s)

Real Estate Investors or Home Buyers

Industry/Entity Type

Real Estate

Contact Information for Business Card

Name, Email, Phone Number, website, email, office address

Colors
EB3D1F
EC4F4E
F09395
F8D3D4
FCEDEE

Requirements
Must have
• Minimalistic, Clean, Modern, Photo
Nice to have
• White and Red Colors

```html
<!DOCTYPE html>
<html lang="en">
<head>
<meta charset="utf-8">
<title>Ember Realty Inc – Business Card</title>
<link rel="stylesheet" href="https://fonts.googleapis.com/css2?family=Jost:wght@400;500&family=Montserrat:wght@600;700&display=swap">
<style>
  :root {
    --canvas-bg: #e4e4e6;
    --card-dark: #2a2a2c;
    --card-dark-soft: #3a3a3d;
    --brand-red: #d90f12;
    --brand-red-deep: #c70a0c;
    --gold: #c9a24a;
    --gold-light: #e3c57a;
    --silver: #c9c9cc;
    --white: #ffffff;
  }
  * { box-sizing: border-box; margin: 0; padding: 0; }
  html, body { width: 1200px; height: 800px; overflow: hidden; }
  body {
    background: var(--canvas-bg);
    font-family: "Jost", "Helvetica Neue", sans-serif;
    position: relative;
  }
  .card {
    position: absolute;
    width: 540px;
    height: 309px;
    border-radius: 18px;
    overflow: hidden;
    top: 246px;
    box-shadow: 0 8px 24px rgba(0,0,0,.18);
  }

  /* Back side */
  .card-back { left: 40px; background: var(--card-dark); }
  .card-back .bottom-edge {
    position: absolute; left: 0; right: 0; bottom: 0; height: 9px;
    background: var(--brand-red);
  }
  .portrait {
    position: absolute; right: 0; top: 0; width: 250px; height: 250px;
    background: radial-gradient(ellipse at 45% 40%, var(--card-dark-soft) 0%, var(--card-dark) 70%);
  }
  .brand-back {
    position: absolute; left: 34px; top: 42px;
    font-family: "Montserrat", sans-serif; font-weight: 700;
    color: var(--brand-red); line-height: 1;
  }
  .brand-back .brand-word { font-size: 50px; letter-spacing: 1px; }
  .brand-back .brand-sub { font-size: 14px; letter-spacing: 7px; margin-top: 6px; padding-left: 4px; }
  .contact {
    position: absolute; left: 36px; top: 152px;
    color: var(--white); font-size: 13.5px; line-height: 1.45;
  }
  .contact .address { margin-bottom: 12px; }
  .contact-row { display: flex; align-items: center; gap: 10px; }
  .contact-row svg { width: 12px; height: 12px; flex: none; }
  .name-band {
    position: absolute; right: 0; bottom: 9px; width: 270px; height: 62px;
    background: linear-gradient(100deg, var(--gold) 0%, var(--gold-light) 55%, var(--gold) 100%);
    clip-path: polygon(22px 0, 100% 0, 100% 100%, 0 100%);
    padding: 10px 0 0 40px;
  }
  .name-band .person-name {
    font-family: "Montserrat", sans-serif; font-weight: 700;
    color: var(--brand-red); font-size: 19px; letter-spacing: .5px;
  }
  .name-band .person-title { color: var(--card-dark); font-size: 13px; margin-top: 1px; padding-left: 30px; }

  /* Front side */
  .card-front {
    left: 620px;
    background: linear-gradient(160deg, var(--brand-red) 0%, var(--brand-red-deep) 100%);
    display: flex; align-items: center; justify-content: center;
  }
  .brand-front {
    font-family: "Montserrat", sans-serif; font-weight: 700;
    color: var(--silver); line-height: 1;
  }
  .brand-front .brand-word { font-size: 74px; letter-spacing: 2px; }
  .brand-front .brand-sub { font-size: 19px; letter-spacing: 8px; margin-top: 10px; padding-left: 70px; white-space: nowrap; }
</style>
</head>
<body>

  <section class="card card-back" aria-label="Business card back">
    <div class="portrait" role="img" aria-label="Portrait photo of the founder in a dark suit"></div>

    <div class="brand-back">
      <div class="brand-word">EMBER</div>
      <div class="brand-sub">REALTY INC</div>
    </div>

    <div class="contact">
      <p class="address">412 Willow Crest Road<br>Juneau, Alaska 99801</p>
      <p class="contact-row">
        <svg viewBox="0 0 12 12" aria-hidden="true"><path fill="#c9a24a" d="M2.5 1l2 2-1 1.3c.7 1.5 1.8 2.6 3.2 3.2L8 6.5l2 2-1.2 1.8C5 10 2 7 1.7 2.2z"/></svg>
        555-210-4821
      </p>
      <p class="contact-row">
        <svg viewBox="0 0 12 12" aria-hidden="true"><rect x="3" y="0.8" width="6" height="10.4" rx="1.2" fill="none" stroke="#c9a24a" stroke-width="1.2"/><circle cx="6" cy="9.4" r=".7" fill="#c9a24a"/></svg>
        555-310-7734
      </p>
      <p class="contact-row">
        <svg viewBox="0 0 12 12" aria-hidden="true"><rect x=".8" y="2.5" width="10.4" height="7" rx="1" fill="#c9a24a"/><path d="M1.2 3l4.8 3.6L10.8 3" fill="none" stroke="#2a2a2c" stroke-width="1"/></svg>
        hello@emberrealty.com
      </p>
      <p class="contact-row">
        <svg viewBox="0 0 12 12" aria-hidden="true"><circle cx="6" cy="6" r="5" fill="none" stroke="#c9a24a" stroke-width="1.2"/><ellipse cx="6" cy="6" rx="2.2" ry="5" fill="none" stroke="#c9a24a" stroke-width="1"/><path d="M1 6h10" stroke="#c9a24a" stroke-width="1"/></svg>
        www.emberrealty.com
      </p>
    </div>

    <div class="name-band">
      <p class="person-name">DANIEL MERCER</p>
      <p class="person-title">Founder &amp; CEO</p>
    </div>
    <div class="bottom-edge"></div>
  </section>

  <section class="card card-front" aria-label="Business card front">
    <div class="brand-front">
      <div class="brand-word">EMBER</div>
      <div class="brand-sub">REALTY INC</div>
    </div>
  </section>

</body>
</html>
```